Can You Help Sell Glass Cabinets with a Banner Ad?

Our New Zealand-based company designs and sells glass cabinets and display cases. 75% of our customers are other businesses who want to display products in their shop or showroom. The other 25% of our customers are householders who want a glass cabinet for their personal collectables. We have been trading 2 years now, and are expanding rapidly. Our website address is www.vitrinelane.co.nz.
We have made a strategic decision to focus on online advertising this year. This is because we want to raise our profile to the greatest number of and widest range of people. For now, this means banner advertising on high traffic New Zealand-based websites in an attempt to generate more traffic to our website. The websites we will initially use are www.dailyharbor.co.nz and www.kowhaipost.co.nz.
We therefore need a set of eye-catching banner ads designed for our online marketing campaign. The three banners required will probably just be variations on a single design.

Banner 1: Top Banner
760x120

Banner 2: Skyscraper
160x600

Banner 3: Medium Rectangle
300x250

Target Market(s)

The primary target market will be retailers who have shops and showrooms. They may not yet know they need a showcase.

Industry/Entity Type

Advertising

Requirements
Must have
• Vitrine Lane logo
"High quality glass cabinets and showcases"
Maybe also "Show your products, not the cabinet"
[Corporate colour is green, as per logo. Secondary colours are orange, purple and grey.]
[Please use New Zealand (British) spelling]

Nice to have
• Please view our website and brochure on the Resources page for the look and feel of our company. In particular we like our logo, so it is possible you can take a lead from this. The logo emblem is designed to be evocative of glass.
The logo spot colour is 41,0,70,10.

```html
<!DOCTYPE html>
<html lang="en-NZ">
<head>
<meta charset="utf-8">
<title>Vitrine Lane – Top Banner Variations</title>
<link rel="stylesheet" href="https://fonts.googleapis.com/css2?family=Questrial&family=Open+Sans+Condensed:wght@300;500&family=Open+Sans:wght@400&display=swap">
<style>
  :root {
    --page-bg: #ffffff;
    --frame-green: #1e6b2c;
    --panel-green-top: #3bb54a;
    --panel-green-bottom: #22863a;
    --divider-green: #5fd06a;
    --band-green-top: #2f9a3f;
    --band-green-bottom: #1f7a30;
    --band-red: #e2252c;
    --text-white: #ffffff;
    --text-soft: #eef7ee;
    --mark-green: #b9dcb3;
    --photo-glass: #c9cfcf;
    --photo-room: #d9d2cc;
    --photo-room-floor: #c0303a;
    --photo-stairs: #c69064;
    --photo-shop: #8d8fa0;
  }
  * { box-sizing: border-box; margin: 0; padding: 0; }
  html, body {
    width: 1200px; height: 509px; overflow: hidden;
    background: var(--page-bg);
  }
  .canvas { position: relative; width: 1200px; height: 509px; }

  .banner {
    position: absolute;
    width: 1162px; height: 184px;
    background: var(--frame-green);
    border-radius: 16px;
    overflow: hidden;
  }
  .banner--green-tagline { left: 20px; top: 38px; }
  .banner--red-tagline { left: 16px; top: 294px; width: 1160px; }

  .brand-panel {
    position: absolute; left: 0; top: 0;
    width: 516px; height: 134px;
    background: linear-gradient(180deg, var(--panel-green-top), var(--panel-green-bottom));
    border-right: 4px solid var(--divider-green);
  }
  .brand-mark {
    position: absolute; left: 34px; top: 46px;
    width: 40px; height: 40px;
    background: var(--mark-green);
  }
  .brand-name {
    position: absolute; left: 104px; top: 28px;
    font-family: "Questrial", "Century Gothic", sans-serif;
    font-size: 42px; letter-spacing: 0.5px;
    color: var(--text-white);
    white-space: nowrap;
  }
  .brand-values {
    position: absolute; left: 106px; top: 82px;
    font-family: "Questrial", "Century Gothic", sans-serif;
    font-size: 26px;
    color: var(--text-soft);
    white-space: nowrap;
  }
  .panel-divider {
    position: absolute; left: 0; top: 134px;
    width: 520px; height: 4px;
    background: var(--divider-green);
  }
  .tagline-band {
    position: absolute; left: 0; top: 138px;
    width: 520px; height: 46px;
    display: flex; align-items: center;
    padding-left: 15px;
    font-family: "Open Sans", sans-serif;
    font-size: 27px; letter-spacing: -0.3px;
    color: var(--text-white);
    text-shadow: 1px 1px 2px rgba(0,0,0,0.45);
    white-space: nowrap;
  }
  .banner--green-tagline .tagline-band {
    background: linear-gradient(180deg, var(--band-green-top), var(--band-green-bottom));
    border-right: 4px solid var(--divider-green);
  }
  .banner--red-tagline .tagline-band {
    background: var(--band-red);
    border-right: 4px solid var(--divider-green);
  }

  .photo { position: absolute; }
  .photo--tall-cabinet {
    left: 526px; top: 6px; width: 58px; height: 126px;
    background: linear-gradient(180deg, #e6eaea, var(--photo-glass));
  }
  .photo--counter {
    left: 594px; top: 6px; width: 170px; height: 126px;
    background: linear-gradient(180deg, var(--photo-room) 0%, #eeeeee 55%, var(--photo-room-floor) 100%);
  }
  .photo--stair-cabinet {
    left: 772px; top: 6px; width: 128px; height: 126px;
    background: linear-gradient(135deg, #efe6da, var(--photo-stairs));
  }
  .photo--shop-floor {
    left: 906px; top: 10px; width: 234px; height: 166px;
    background: linear-gradient(180deg, #dde2ea 0%, var(--photo-shop) 60%, #4d5572 100%);
  }

  .product-line {
    position: absolute; left: 546px; top: 140px;
    width: 340px;
    text-align: center;
    font-family: "Open Sans Condensed", "Arial Narrow", sans-serif;
    font-weight: 500;
    font-size: 23px; line-height: 22px;
    color: var(--text-white);
    text-shadow: 1px 1px 2px rgba(0,0,0,0.5);
  }
</style>
</head>
<body>
<main class="canvas">

  <section class="banner banner--green-tagline" aria-label="Top banner, green tagline">
    <div class="brand-panel">
      <span class="brand-mark" aria-hidden="true"></span>
      <p class="brand-name">VITRINE LANE</p>
      <p class="brand-values">design strength value</p>
    </div>
    <div class="panel-divider"></div>
    <p class="tagline-band">Show your products, not the cabinet</p>
    <div class="photo photo--tall-cabinet" role="img" aria-label="Photo of a tall glass display cabinet with shelves"></div>
    <div class="photo photo--counter" role="img" aria-label="Photo of a glass counter showcase in a bright showroom with red floor"></div>
    <div class="photo photo--stair-cabinet" role="img" aria-label="Photo of a glass cabinet beside a timber staircase"></div>
    <div class="photo photo--shop-floor" role="img" aria-label="Photo of a retail shop floor fitted with glass showcases"></div>
    <p class="product-line">High quality glass cabinets and<br>showcases</p>
  </section>

  <section class="banner banner--red-tagline" aria-label="Top banner, red tagline">
    <div class="brand-panel">
      <span class="brand-mark" aria-hidden="true"></span>
      <p class="brand-name">VITRINE LANE</p>
      <p class="brand-values">design strength value</p>
    </div>
    <div class="panel-divider"></div>
    <p class="tagline-band">Show your products, not the cabinet</p>
    <div class="photo photo--tall-cabinet" role="img" aria-label="Photo of a tall glass display cabinet with shelves"></div>
    <div class="photo photo--counter" role="img" aria-label="Photo of a glass counter showcase in a bright showroom with red floor"></div>
    <div class="photo photo--stair-cabinet" role="img" aria-label="Photo of a glass cabinet beside a timber staircase"></div>
    <div class="photo photo--shop-floor" role="img" aria-label="Photo of a retail shop floor fitted with glass showcases"></div>
    <p class="product-line">High quality glass cabinets and<br>showcases</p>
  </section>

</main>
</body>
</html>
```